Global social media analytics company needs business card design

We need an updated business card design to align with our new website - brightquillo.net -

I would also like a favicon designed as well.

Target Market(s)

CEOs, CMOs go big companies

Industry/Entity Type

Business

Contact Information for Business Card

Room for the following:
Address
Main telephone
Direct telephone or cell phone
twitter handle

Colors
aaaaaa

Requirements
Must have
• Attention to detail; style.
• Use the logo color from our website - which is gray

```html
<!DOCTYPE html>
<html lang="en">
<head>
<meta charset="utf-8">
<title>brightquillo stationery</title>
<link rel="stylesheet" href="https://fonts.googleapis.com/css2?family=Lato:wght@400;700;900&family=Arimo:wght@400;700&display=swap">
<style>
:root{
  --stage:#d6d6d6;
  --paper:#ffffff;
  --brand-blue:#3b5fad;
  --brand-gray:#3d3d3d;
  --ink:#2f2f2f;
  --muted:#555555;
  --rule:#b9b9b9;
  --sign-name:#3a3f8f;
  --stamp:#7d6fb0;
}
*{box-sizing:border-box;margin:0;padding:0}
html,body{width:1200px;height:776px;overflow:hidden}
body{background:var(--stage);position:relative;font-family:"Arimo",Arial,sans-serif;color:var(--ink)}
.sheet{position:absolute;background:var(--paper)}
.wordmark{display:flex;align-items:center;gap:8px;font-family:"Lato",sans-serif;font-weight:900;color:var(--brand-gray);letter-spacing:-.2px}
.wordmark .dot{border-radius:50%;background:var(--brand-gray);flex:none}
.contacts{position:absolute;display:grid;grid-template-columns:auto auto;column-gap:14px;row-gap:6px;font-family:"Lato",sans-serif;color:var(--muted)}
.contact{display:flex;align-items:flex-start;gap:6px;line-height:1.25}
.contact svg{flex:none;fill:var(--brand-blue)}

/* letterhead */
.letterhead{left:22px;top:42px;width:510px;height:660px}
.letterhead .wordmark{position:absolute;left:43px;top:22px;font-size:18px}
.letterhead .wordmark .dot{width:34px;height:34px}
.letterhead .contacts{left:270px;top:50px;font-size:7.5px}
.contact svg{width:11px;height:11px}
.meta{position:absolute;top:137px;font-size:7px;line-height:1.35}
.meta b{display:block}
.meta.date{left:46px}
.meta.subject{left:150px}
.meta-rule{position:absolute;left:46px;top:170px;width:422px;height:1px;background:var(--rule)}
.body-copy{position:absolute;left:48px;top:194px;width:420px;font-size:7px;line-height:11.6px;color:#333}
.body-copy p{margin-bottom:11.6px}
.signature{position:absolute;left:280px;top:530px;width:90px;height:70px;background:linear-gradient(135deg,#f3f3f3,#e6e6e6)}
.stamp{position:absolute;left:356px;top:522px;width:78px;height:78px}
.signer{position:absolute;right:16px;top:614px;font-family:"Lato",sans-serif;font-size:11px;color:var(--sign-name)}
.letterhead .band{position:absolute;left:0;bottom:0;width:100%;height:20px;background:var(--brand-blue)}

/* business cards */
.card-front{left:742px;top:98px;width:212px;height:119px;background:var(--brand-blue);display:flex;align-items:center;justify-content:center}
.card-front .wordmark{color:#fff;font-size:14px}
.card-front .wordmark .dot{background:#fff;width:26px;height:26px}
.card-back{left:742px;top:277px;width:206px;height:122px}
.card-back .wordmark{position:absolute;left:10px;top:8px;font-size:10px;gap:5px}
.card-back .wordmark .dot{width:18px;height:18px}
.person{position:absolute;right:8px;top:34px;text-align:right;font-family:"Lato",sans-serif}
.person .name{font-size:12px;font-weight:700;color:var(--brand-gray)}
.person .role{font-size:7.5px;color:var(--brand-blue)}
.card-back .contacts{left:10px;top:85px;font-size:5.5px;row-gap:3px;column-gap:20px}
.card-back .contact svg{width:8px;height:8px}

/* envelope */
.envelope{left:589px;top:455px;width:570px;height:243px}
.envelope .wordmark{position:absolute;left:28px;top:30px;font-size:18px}
.envelope .wordmark .dot{width:34px;height:34px}
.envelope .contacts{left:337px;top:30px;font-size:7.5px;column-gap:22px;row-gap:6px}
.envelope .band{position:absolute;left:0;bottom:0;width:100%;height:4px;background:var(--brand-blue)}
</style>
</head>
<body>
<svg width="0" height="0" style="position:absolute" aria-hidden="true">
  <symbol id="i-phone" viewBox="0 0 12 12"><circle cx="6" cy="6" r="6"/><path d="M4 3.2l1 1.2-.6.7c.4.9 1 1.5 1.9 1.9l.7-.6 1.2 1-.6 1c-2.4-.3-4.3-2.2-4.6-4.6z" fill="#fff"/></symbol>
  <symbol id="i-mail" viewBox="0 0 12 12"><circle cx="6" cy="6" r="6"/><rect x="3.3" y="4" width="5.4" height="4" fill="#fff"/><path d="M3.3 4L6 6.2 8.7 4" stroke="#3b5fad" stroke-width=".6" fill="none"/></symbol>
  <symbol id="i-web" viewBox="0 0 12 12"><circle cx="6" cy="6" r="6"/><circle cx="6" cy="6" r="2.8" fill="none" stroke="#fff" stroke-width=".8"/><path d="M3.2 6h5.6M6 3.2v5.6" stroke="#fff" stroke-width=".6"/></symbol>
  <symbol id="i-pin" viewBox="0 0 12 12"><circle cx="6" cy="6" r="6"/><path d="M6 9.2L4 6.2a2.2 2.2 0 1 1 4 0z" fill="#fff"/><circle cx="6" cy="5.2" r=".8"/></symbol>
</svg>

<section class="sheet letterhead">
  <div class="wordmark"><span class="dot"></span>brightquillo</div>
  <div class="contacts">
    <div class="contact"><svg><use href="#i-phone"/></svg>+1 555 014 7720</div>
    <div class="contact"><svg><use href="#i-web"/></svg>www.brightquillo.net</div>
    <div class="contact"><svg><use href="#i-mail"/></svg>info@brightquillo.net</div>
    <div class="contact"><svg><use href="#i-pin"/></svg><span>220 Harbor Row<br>3rd Fl Lowell, MA 01852&nbsp; USA</span></div>
  </div>
  <div class="meta date"><b>Date:</b>06/02/2015</div>
  <div class="meta subject"><b>Subject:</b>Lorem ipsum dolor sit amet, consectuer adipiscing elit.</div>
  <div class="meta-rule"></div>
  <div class="body-copy">
    <p>Lorem ipsum dolor sit amet, consectetur adipisicing elit, sed do eiusmod tempor incididunt ut labore et dolore magna aliqua. Ut enim ad minim veniam, quis nostrud exercitation ullamco laboris nisi ut aliquip ex ea commodo consequat. Duis aute irure dolor in reprehenderit in voluptate velit esse cillum dolore eu fugiat nulla pariatur.</p>
    <p>Excepteur sint occaecat cupidatat non proident, sunt in culpa qui officia deserunt mollit anim id est laborum. Lorem ipsum dolor sit amet, consectetur adipisicing elit, sed do eiusmod tempor incididunt ut labore et dolore magna aliqua. Ut enim ad minim veniam, quis nostrud exercitation ullamco laboris nisi ut aliquip ex ea commodo consequat.</p>
    <p>Duis aute irure dolor in reprehenderit in voluptate velit esse cillum dolore eu fugiat nulla pariatur. Excepteur sint occaecat cupidatat non proident, sunt in culpa qui officia deserunt mollit anim id est laborum.</p>
    <p>Lorem ipsum dolor sit amet, consectetur adipisicing elit, sed do eiusmod tempor incididunt ut labore et dolore magna aliqua. Ut enim ad minim veniam, quis nostrud exercitation ullamco laboris nisi ut aliquip ex ea commodo consequat. Duis aute irure dolor in reprehenderit in voluptate velit esse cillum dolore eu fugiat nulla pariatur. Excepteur sint occaecat cupidatat non proident, sunt in culpa qui officia deserunt mollit anim id est laborum.</p>
    <p>Lorem ipsum dolor sit amet, consectetur adipisicing elit, sed do eiusmod tempor incididunt ut labore et dolore magna aliqua. Ut enim ad minim veniam, quis nostrud exercitation ullamco laboris nisi ut aliquip ex ea commodo consequat. Duis aute irure dolor in reprehenderit in voluptate velit esse cillum dolore eu fugiat nulla pariatur. Excepteur sint occaecat cupidatat non proident, sunt in culpa qui officia deserunt mollit anim id est laborum.</p>
    <p>Excepteur sint occaecat cupidatat non proident, sunt in culpa qui officia deserunt mollit anim id est laborum. Lorem ipsum dolor sit amet, consectetur adipisicing elit, sed do eiusmod tempor incididunt ut labore et dolore magna aliqua. Ut enim ad minim veniam, quis nostrud exercitation ullamco laboris nisi ut aliquip ex ea commodo consequat.</p>
    <p>Duis aute irure dolor in reprehenderit in voluptate velit esse cillum dolore eu fugiat nulla pariatur. Excepteur sint occaecat cupidatat non proident, sunt in culpa qui officia deserunt mollit anim id est laborum.</p>
  </div>
  <div class="signature" role="img" aria-label="Handwritten signature of the founder"></div>
  <svg class="stamp" viewBox="0 0 78 78" aria-hidden="true">
    <circle cx="39" cy="39" r="37" fill="none" stroke="var(--stamp)" stroke-width="2"/>
    <circle cx="39" cy="39" r="24" fill="none" stroke="var(--stamp)" stroke-width="1.2"/>
  </svg>
  <div class="signer">Marcus Hale, Founder &amp; CEO</div>
  <div class="band"></div>
</section>

<section class="sheet card-front">
  <div class="wordmark"><span class="dot"></span>brightquillo</div>
</section>

<section class="sheet card-back">
  <div class="wordmark"><span class="dot"></span>brightquillo</div>
  <div class="person"><div class="name">Marcus Hale</div><div class="role">Founder &amp; CEO</div></div>
  <div class="contacts">
    <div class="contact"><svg><use href="#i-phone"/></svg>+1 555 014 7720</div>
    <div class="contact"><svg><use href="#i-web"/></svg>www.brightquillo.net</div>
    <div class="contact"><svg><use href="#i-mail"/></svg>info@brightquillo.net</div>
    <div class="contact"><svg><use href="#i-pin"/></svg><span>220 Harbor Row<br>3rd Fl Lowell, MA 01852&nbsp; USA</span></div>
  </div>
</section>

<section class="sheet envelope">
  <div class="wordmark"><span class="dot"></span>brightquillo</div>
  <div class="contacts">
    <div class="contact"><svg><use href="#i-phone"/></svg>+1 555 014 7720</div>
    <div class="contact"><svg><use href="#i-web"/></svg>www.brightquillo.net</div>
    <div class="contact"><svg><use href="#i-mail"/></svg>info@brightquillo.net</div>
    <div class="contact"><svg><use href="#i-pin"/></svg><span>220 Harbor Row<br>3rd Fl Lowell, MA 01852&nbsp; USA</span></div>
  </div>
  <div class="band"></div>
</section>
</body>
</html>
```